New Church Home Page and Content Page Design

Our church, Harbor Light Baptist Church www.hlbtvkx.org, needs an update for our online presence. The homepage design should provide the following 4 pieces of information above the fold:
1. Church location - 47 Pinecrest Hollow Lane in Larkhaven, Larkhaven County, USA.
2. Service times and types Sunday school, children's church, etc..
3. A space for some text describing us and our beliefs - a Bible believing independent Baptist church.
4. photos of our members to give visitors an impression of what kind of people attend our church - a friendly group of culturally diverse people who love Jesus.

In addition to the homepage we need a design for internal pages of general content. The content page design should provide a lot of room for content and prominent navigation area. We will use this design to host pages with content such as:
A full description of our beliefs
A photo gallery
An event calendar
Embedded audio and video of past sermons
A member directory
etc.
Updates

Thanks everyone for your submissions. I'll be meeting with our Pastor tomorrow. I am working as fast as I can to review all the designs and come up with a short list for him. A decision should be close behind.

Target Market(s)

Local people looking for a church.

Industry/Entity Type

Church

Requirements
Must have
• 1. Place to show church location - Westchester county, New York State, USA.
2. Place to list service times and types.
3. A space for some text describing us and our beliefs.
4. A place to display photos of our members (see also the nice to have section)
Nice to have
• Would be great if the member photos (#4 in must have section) displayed the images in some innovative way. I rather not have an ordinary carousel of images.

```html
<!DOCTYPE html>
<html lang="en">
<head>
<meta charset="utf-8">
<title>Harbor Light Baptist Church</title>
<link href="https://fonts.googleapis.com/css2?family=Open+Sans:wght@400;600;700;800&family=Mulish:wght@400;500;600&family=Lora:ital@1&display=swap" rel="stylesheet">
<style>
:root{
  --navy:#27344d;
  --navy-deep:#1f2a3e;
  --green:#76a03b;
  --paper:#f3f2ec;
  --ink:#3a3f4a;
  --muted:#5d6270;
  --rule:#c9c9c4;
  --black:#0c0c0c;
}
*{margin:0;padding:0;box-sizing:border-box}
html,body{width:923px;height:1200px;overflow:hidden}
body{position:relative;background:var(--paper);font-family:"Mulish",sans-serif;color:var(--ink)}
.abs{position:absolute}

.site-header{position:absolute;left:0;top:0;width:923px;height:78px;background:#fff}
.brand{position:absolute;left:132px;top:17px;display:flex;align-items:center;gap:8px}
.brand-mark{width:12px;height:12px;background:var(--navy)}
.brand-name{font-family:"Open Sans",sans-serif;font-weight:700;font-size:14px;line-height:16px;color:var(--navy)}
.search{position:absolute;left:580px;top:10px;width:211px;height:26px;border:1px solid #9aa0aa;background:#fff}
.search span{position:absolute;left:8px;top:6px;font-size:9px;font-style:italic;color:#8a8f99}
.search svg{position:absolute;right:7px;top:6px}
.main-nav{position:absolute;top:52px;left:0;font-family:"Mulish",sans-serif;font-weight:600;font-size:9.5px;color:#111;letter-spacing:.1px}
.main-nav a{position:absolute;white-space:nowrap;color:#111;text-decoration:none}

.hero{position:absolute;left:0;top:78px;width:923px;height:342px;background:linear-gradient(100deg,#e4e3e0 0%,#cfcdc8 35%,#9a8f86 58%,#5b4b43 75%,#cfccc7 100%)}
.hero-title{position:absolute;left:128px;font-family:"Open Sans",sans-serif;font-weight:800;font-size:57px;line-height:1;letter-spacing:-1.5px}
.hero-title.light{top:140px;color:#fff}
.hero-title.dark{top:212px;color:var(--navy-deep)}
.hero-arrow{position:absolute;top:148px;width:32px;height:58px;background:rgba(60,72,96,.85)}
.hero-arrow.prev{left:0}.hero-arrow.next{right:0}
.hero-arrow svg{position:absolute;left:8px;top:17px}

.verse-band{position:absolute;left:0;top:420px;width:923px;height:56px;background:var(--green)}
.verse-band::before,.verse-band::after{content:"";position:absolute;left:0;width:923px;border-top:1px dashed rgba(255,255,255,.85)}
.verse-band::before{top:8px}.verse-band::after{top:47px}
.verse-band p{position:absolute;left:0;width:923px;top:20px;text-align:center;font-family:"Lora",serif;font-style:italic;font-size:10.5px;color:#fff}

.promo{position:absolute;top:500px;width:210px;height:131px;overflow:hidden}
.promo .photo{position:absolute;inset:0}
.promo h3{position:absolute;right:6px;top:62px;font-family:"Open Sans",sans-serif;font-weight:700;font-size:28px;color:#fff;letter-spacing:-.5px}
.promo .bar{position:absolute;right:0;bottom:0;width:172px;height:30px;background:rgba(39,52,77,.88);color:#fff;font-size:10px;line-height:30px;padding-left:12px}
.promo .bar svg{position:absolute;right:8px;top:6px}

.section-title{position:absolute;font-family:"Mulish",sans-serif;font-weight:500;font-size:14.5px;color:var(--navy);text-transform:uppercase}
.map{position:absolute;left:132px;top:682px;width:210px;height:100px;background:linear-gradient(135deg,#e4e2dc,#d6d4cc)}
.location-text{position:absolute;left:132px;top:790px;width:215px;font-size:8.6px;line-height:12.6px;color:var(--muted)}

.services{position:absolute;left:356px;top:680px;width:210px;list-style:none}
.services li{height:40.3px;border-bottom:1px solid var(--rule);padding-top:2px}
.services b{display:block;font-weight:500;font-size:11px;color:var(--navy)}
.services small{display:block;font-size:8px;color:var(--muted);margin-top:2px}

.beliefs{position:absolute;left:580px;top:680px;width:215px;list-style:none}
.beliefs li{position:relative;padding-left:19px;margin-bottom:7px}
.beliefs svg{position:absolute;left:0;top:2px}
.beliefs b{display:block;font-weight:500;font-size:11px;color:var(--navy)}
.beliefs p{font-size:8.6px;line-height:12.6px;color:var(--muted);margin-top:1px}

.event-photo{position:absolute;left:132px;top:886px;width:152px;height:129px;background:linear-gradient(160deg,#6d8a4a,#9aa77c 55%,#8c7562)}
.event-date{position:absolute;left:298px;top:883px;width:24px;text-align:center;color:var(--green)}
.event-date b{display:block;font-weight:400;font-size:19px;line-height:1}
.event-date small{display:block;font-size:8px}
.event-name{position:absolute;left:333px;top:888px;font-size:11px;color:var(--navy)}
.event-time{position:absolute;left:333px;top:903px;font-size:8px;color:var(--muted)}
.event-text{position:absolute;left:298px;top:921px;width:155px;font-size:8.6px;line-height:12.6px;color:var(--muted)}
.btn{position:absolute;background:var(--green);color:#fff;text-align:center;font-size:10.5px;font-weight:500}
.btn.more{left:298px;top:994px;width:59px;height:21px;line-height:21px}

.video{position:absolute;left:475px;top:886px;width:316px;height:129px;background:linear-gradient(120deg,#c9a683,#b9926f 45%,#7a8f9e);overflow:hidden}
.video-controls{position:absolute;left:0;bottom:0;width:316px;height:23px;background:rgba(10,10,10,.85)}
.video-controls .track{position:absolute;left:32px;top:10px;width:245px;height:3px;background:#444}
.video-controls .track i{position:absolute;left:0;top:0;width:58px;height:3px;background:#ddd}

.site-footer{position:absolute;left:0;top:1049px;width:923px;height:118px;background:var(--navy)}
.footer-title{position:absolute;top:18px;font-size:13px;font-weight:500;color:#fff;text-transform:uppercase}
.footer-title.reach{color:#c8ccd4}
.btn.signup{left:132px;top:48px;width:181px;height:25px;line-height:25px;font-size:11px}
.reach-line{position:absolute;left:356px;font-size:10px;color:#fff;line-height:17px;white-space:nowrap}
.reach-line span{display:inline-block;width:20px;color:#c8ccd4}
.social{position:absolute;top:53px;display:flex;gap:5px;left:628px}
.social i{display:block;width:21px;height:21px;border-radius:50%;background:#fff;position:relative}
.social i svg{position:absolute;left:5px;top:6px}
.copyright{position:absolute;left:0;top:1167px;width:923px;height:33px;background:var(--black);color:#fff;font-size:8px;padding:9px 0 0 132px}
</style>
</head>
<body>

<header class="site-header">
  <div class="brand">
    <span class="brand-mark"></span>
    <span class="brand-name">Harbor Light<br>Baptist Church</span>
  </div>
  <div class="search"><span>search</span>
    <svg width="12" height="12" viewBox="0 0 12 12"><circle cx="5" cy="5" r="3.8" fill="none" stroke="#8a8f99" stroke-width="1.6"/><line x1="7.8" y1="7.8" x2="11" y2="11" stroke="#8a8f99" stroke-width="1.8"/></svg>
  </div>
  <nav class="main-nav">
    <a style="left:352px">CONTACT US</a>
    <a style="left:437px">CALENDAR</a>
    <a style="left:514px">MINISTRIES</a>
    <a style="left:592px">SERVICE TIMES</a>
    <a style="left:684px">SERMONS AND MEDIA</a>
  </nav>
</header>

<section class="hero" role="img" aria-label="Close-up of hands clasped in prayer over an open Bible">
  <div class="hero-title light">THE POWER</div>
  <div class="hero-title dark">OF PRAYER</div>
  <div class="hero-arrow prev"><svg width="14" height="24" viewBox="0 0 14 24"><polyline points="11,2 3,12 11,22" fill="none" stroke="#fff" stroke-width="2"/></svg></div>
  <div class="hero-arrow next"><svg width="14" height="24" viewBox="0 0 14 24"><polyline points="3,2 11,12 3,22" fill="none" stroke="#fff" stroke-width="2"/></svg></div>
</section>

<div class="verse-band"><p>1 John 5:4 &nbsp;4 For everyone who has been born of God overcomes the world. And this is the victory that has overcome the world—our faith.</p></div>

<article class="promo" style="left:132px">
  <div class="photo" role="img" aria-label="Church couple standing in front of a stone wall" style="background:linear-gradient(135deg,#8d8a80,#5e5a52 55%,#3f4a3a)"></div>
  <h3>MINISTRIES</h3>
  <div class="bar">Know more about ministries<svg width="18" height="18" viewBox="0 0 18 18"><circle cx="9" cy="9" r="8" fill="none" stroke="#fff" stroke-width="1.5"/><path d="M5 9h8M10 6l3 3-3 3" fill="none" stroke="#fff" stroke-width="1.5"/></svg></div>
</article>
<article class="promo" style="left:356px">
  <div class="photo" role="img" aria-label="Pastor greeting a visitor outdoors" style="background:linear-gradient(135deg,#6f8f64,#b7b7ad 50%,#3d4560)"></div>
  <h3>UPDATES</h3>
  <div class="bar" style="padding-left:18px">Read our Pastor's updates<svg width="18" height="18" viewBox="0 0 18 18"><circle cx="9" cy="9" r="8" fill="none" stroke="#fff" stroke-width="1.5"/><path d="M5 9h8M10 6l3 3-3 3" fill="none" stroke="#fff" stroke-width="1.5"/></svg></div>
</article>
<article class="promo" style="left:580px">
  <div class="photo" role="img" aria-label="Stone church building among autumn trees" style="background:linear-gradient(160deg,#50623a,#6d5e4f 50%,#8c7a3e)"></div>
  <h3>FIRST VISIT</h3>
  <div class="bar" style="padding-left:14px">Become part of our Church<svg width="18" height="18" viewBox="0 0 18 18"><circle cx="9" cy="9" r="8" fill="none" stroke="#fff" stroke-width="1.5"/><path d="M5 9h8M10 6l3 3-3 3" fill="none" stroke="#fff" stroke-width="1.5"/></svg></div>
</article>

<h2 class="section-title" style="left:131px;top:651px">Church Location</h2>
<div class="map" role="img" aria-label="Street map showing the church location"></div>
<p class="location-text">Located on 47 Pinecrest Hollow Lane in Larkhaven, Larkhaven County - Exit 14 off the Briar Hill Parkway - Corner of Elm St. (South 88) and Pinecrest Hollow Lane.</p>

<h2 class="section-title" style="left:355px;top:651px">Services</h2>
<ul class="services">
  <li><b>Coffee and Fellowship</b><small>Sunday | 9:45 am</small></li>
  <li><b>Sunday School</b><small>Sunday | 10:00 am</small></li>
  <li><b>Sunday Morning Worship</b><small>Sunday | 11:00 am</small></li>
  <li><b>Wednesday Bible Study &amp; Prayer Time</b><small>Wednesday | 17:00 pm</small></li>
</ul>

<h2 class="section-title" style="left:579px;top:651px">Core Beliefs</h2>
<ul class="beliefs">
  <li><svg width="11" height="14" viewBox="0 0 11 14"><path d="M5.5 0v14M0 4h11" stroke="#76a03b" stroke-width="2"/></svg><b>Core Belief One</b><p>Lorem Ipsum has been the industry's standard dummy text ever since the.</p></li>
  <li><svg width="11" height="14" viewBox="0 0 11 14"><path d="M5.5 0v14M0 4h11" stroke="#76a03b" stroke-width="2"/></svg><b>Core Belief Two</b><p>Lorem Ipsum has been the industry's standard dummy text ever since the. Lorem Ipsum has been the industry's standard dummy text.</p></li>
  <li><svg width="11" height="14" viewBox="0 0 11 14"><path d="M5.5 0v14M0 4h11" stroke="#76a03b" stroke-width="2"/></svg><b>Core Belief Three</b><p>Lorem Ipsum has been the industry's standard dummy text ever since the. Lorem Ipsum has been the industry's standard dummy text.</p></li>
</ul>

<h2 class="section-title" style="left:131px;top:855px">Upcoming Events</h2>
<div class="event-photo" role="img" aria-label="Members sharing a picnic at outdoor tables"></div>
<div class="event-date"><b>30</b><small>APR</small></div>
<div class="event-name">CHURCH GATHERING</div>
<div class="event-time">Sunday | 9:30 am</div>
<p class="event-text">Lorem Ipsum has been the industry's standard dummy text ever since the 1500s, when an unknown printer took a galley of type and scrambled it to make a type specimen book.</p>
<div class="btn more">MORE</div>

<h2 class="section-title" style="left:475px;top:855px">Latest Videos</h2>
<div class="video" role="img" aria-label="Video of children singing in the children's church">
  <div class="video-controls">
    <svg class="abs" style="left:14px;top:7px" width="8" height="9" viewBox="0 0 8 9"><polygon points="0,0 8,4.5 0,9" fill="#fff"/></svg>
    <div class="track"><i></i></div>
    <svg class="abs" style="right:8px;top:6px" width="11" height="11" viewBox="0 0 11 11"><path d="M1 10L10 1M6 1h4v4M1 6v4h4" fill="none" stroke="#999" stroke-width="1"/></svg>
  </div>
</div>

<footer class="site-footer">
  <div class="footer-title" style="left:132px">Signup to our Newsletter</div>
  <div class="btn signup">EMAIL SIGNUP</div>
  <div class="footer-title reach" style="left:356px">Reach Us</div>
  <div class="reach-line" style="top:45px"><span>[a]</span>47 Pinecrest Hollow Lane in Larkhaven</div>
  <div class="reach-line" style="top:62px"><span></span>Larkhaven County, USA</div>
  <div class="reach-line" style="top:81px"><span>[p]</span>914-555-0147</div>
  <div class="footer-title" style="left:628px">Connect with Us</div>
  <div class="social">
    <i aria-label="Social network"></i>
    <i aria-label="Social network"></i>
    <i aria-label="Video channel"></i>
    <i aria-label="Photo sharing"></i>
    <i aria-label="Email"><svg width="11" height="9" viewBox="0 0 11 9"><rect x="0.5" y="0.5" width="10" height="8" fill="none" stroke="#27344d"/><path d="M0.5 0.5l5 4.5 5-4.5" fill="none" stroke="#27344d"/></svg></i>
  </div>
</footer>
<div class="copyright">© Copyright 2014 Harbor Light Baptist Church. All rights reserved.</div>

</body>
</html>
```